Business card design needed

Chasing a very simplistic modern design with a logo incorporating "TRV".
I'm starting a plumbing business.
I do water, sanitary and drainage plumbing that will cover residential, commercial, rental, rural, excavation, new housing and all maintanence requirements.

Industry/Entity Type

Business

Contact Information for Business Card

TRV PLUMBING SERVICES
DEAN HOLLOWBY - LICENSED PLUMBER
PHONE: 0481926574
E-MAIL: hollodt7@wirelane.com
NORTHERN SUBURBS

Requirements
Must have
• lower case email address

```html
<!DOCTYPE html>
<html lang="en">
<head>
<meta charset="utf-8">
<title>TRV Plumbing Services – Business Card</title>
<link rel="stylesheet" href="https://fonts.googleapis.com/css2?family=Raleway:wght@400&display=swap">
<style>
  :root {
    --paper: #ffffff;
    --ink: #111111;
    --accent-red: #b3121b;
    --stripe-red: #e0202a;
    --stripe-dark: #1a1a1a;
    --weave-light: #6d767e;
    --weave-mid: #59626a;
    --weave-dark: #454c53;
  }
  html, body {
    margin: 0;
    padding: 0;
    width: 1200px;
    height: 741px;
    overflow: hidden;
    background: var(--paper);
  }
  .card {
    position: relative;
    width: 1200px;
    height: 741px;
    background: var(--paper);
    font-family: "Raleway", "Helvetica Neue", Arial, sans-serif;
    color: var(--ink);
  }
  .card__texture {
    position: absolute;
    left: 0;
    top: 0;
    width: 1200px;
    height: 423px;
    background: linear-gradient(100deg, var(--weave-light) 0%, var(--weave-mid) 45%, var(--weave-dark) 100%);
  }
  .card__rule {
    position: absolute;
    left: 0;
    width: 1200px;
  }
  .card__rule--dark { top: 421px; height: 3px; background: var(--stripe-dark); }
  .card__rule--red { top: 424px; height: 6px; background: var(--stripe-red); }
  .card__name-mark {
    position: absolute;
    right: 60px;
    top: 270px;
    margin: 0;
    font-weight: 400;
    font-size: 120px;
    line-height: 1;
    color: var(--ink);
  }
  .card__details {
    position: absolute;
    left: 0;
    top: 438px;
    width: 1206px;
    margin: 0;
    text-align: center;
    font-weight: 400;
    font-size: 45px;
    line-height: 52px;
    letter-spacing: -0.3px;
  }
  .card__details p { margin: 0; }
  .card__business { color: var(--accent-red); }
  .card__contact .gap { display: inline-block; width: 24px; }
</style>
</head>
<body>
  <main class="card">
    <div class="card__texture" role="img" aria-label="Woven grey-blue fabric texture backdrop"></div>
    <h1 class="card__name-mark">TRV</h1>
    <div class="card__rule card__rule--dark"></div>
    <div class="card__rule card__rule--red"></div>
    <section class="card__details">
      <p class="card__business">TRV Plumbing Services</p>
      <p class="card__person">Dean Hollowby - Licensed Plumber</p>
      <p class="card__contact">Phone: 0481926574<span class="gap"></span>email: hollodt7@wirelane.com</p>
      <p class="card__area">NORTHERN SUBURBS</p>
    </section>
  </main>
</body>
</html>
```